Tavlune

I'd like new business card design options. I'll need to provide updated contact info although after the deign is complete. We are in IT, specifically in the data backup, archiving and disaster recovery verticals.

Business

```html
<!DOCTYPE html>
<html lang="en">
<head>
<meta charset="utf-8">
<title>Tavlune Business Card</title>
<link rel="stylesheet" href="https://fonts.googleapis.com/css2?family=Roboto+Condensed:wght@400;500;700&display=swap">
<style>
  :root {
    --navy: #1a5aa6;
    --cyan-light: #00f4ff;
    --cyan-deep: #00c2f2;
    --ink: #1c1c1c;
    --link: #2a8ad8;
    --white: #ffffff;
    --page: #ffffff;
  }
  * { margin: 0; padding: 0; box-sizing: border-box; }
  html, body {
    width: 1200px; height: 800px; overflow: hidden;
    background: var(--page);
    font-family: "Roboto Condensed", "Arial Narrow", sans-serif;
  }
  .card {
    position: absolute; left: 52px; top: 88px;
    width: 1096px; height: 624px;
    border-radius: 40px; overflow: hidden;
    border: 1px solid var(--navy);
    background: var(--white);
  }
  .card-art { position: absolute; inset: 0; }
  .brand-mark {
    position: absolute; left: 70px; top: 48px;
    width: 92px; height: 92px; border-radius: 50%;
    background: var(--navy);
  }
  .brand-name {
    position: absolute; left: 182px; top: 64px;
    font-size: 60px; font-weight: 700; letter-spacing: 12px;
    color: var(--navy); line-height: 1;
  }
  .contact-list { position: absolute; left: 230px; top: 176px; list-style: none; }
  .contact-item {
    position: absolute; left: 0; display: flex; align-items: center; gap: 14px;
    font-size: 26px; color: var(--ink); line-height: 30px; white-space: nowrap;
  }
  .contact-item svg { width: 32px; height: 32px; flex: none; }
  .contact-address { top: 0; align-items: flex-start; }
  .contact-address svg { margin-top: 6px; }
  .contact-phone { top: 73px; }
  .contact-fax { top: 122px; }
  .contact-web { top: 172px; font-size: 24px; }
  .divider {
    position: absolute; left: 600px; top: 76px;
    width: 4px; height: 422px; background: var(--navy);
  }
  .person { position: absolute; left: 608px; top: 268px; width: 460px; text-align: center; }
  .person-name {
    font-size: 38px; color: var(--navy); font-weight: 400; line-height: 1;
    white-space: nowrap;
  }
  .person-name strong { font-weight: 700; }
  .person-title { margin-top: 14px; font-size: 28px; font-weight: 700; color: var(--ink); white-space: nowrap; }
  .person-email {
    position: absolute; left: 662px; top: 398px;
    display: flex; align-items: center; gap: 14px;
    font-size: 25px; color: var(--link); white-space: nowrap;
  }
  .person-email svg { width: 32px; height: 32px; }
  .products { position: absolute; right: 18px; top: 28px; width: 184px; text-align: right; color: var(--white); }
  .products-label {
    text-align: left; font-size: 13px; font-weight: 700; letter-spacing: 0.5px;
    padding-bottom: 3px; border-bottom: 1px solid var(--white);
  }
  .product { font-size: 31px; font-weight: 700; line-height: 37px; padding-right: 14px; position: relative; }
  .product sup { position: absolute; right: -4px; top: -2px; font-size: 15px; font-weight: 500; }
  .services { position: absolute; left: 50px; top: 452px; list-style: none; color: var(--white); }
  .service { font-size: 27px; font-weight: 500; line-height: 48px; padding-left: 26px; position: relative; white-space: nowrap; }
  .service::before {
    content: ""; position: absolute; left: 0; top: 21px;
    width: 6px; height: 6px; border-radius: 50%; background: var(--white);
  }
</style>
</head>
<body>
<div class="card">
  <svg class="card-art" viewBox="0 0 1096 624" preserveAspectRatio="none" aria-hidden="true">
    <defs>
      <linearGradient id="cyanFill" x1="0" y1="0" x2="0" y2="1">
        <stop offset="0" stop-color="#00f4ff"/>
        <stop offset="1" stop-color="#00c2f2"/>
      </linearGradient>
      <linearGradient id="cornerFill" x1="0" y1="0" x2="1" y2="1">
        <stop offset="0" stop-color="#00cdf7"/>
        <stop offset="1" stop-color="#00f4ff"/>
      </linearGradient>
    </defs>
    <polygon points="790,0 1096,0 1096,232" fill="url(#cornerFill)"/>
    <polygon points="748,0 792,0 1096,232 1096,270" fill="#1a5aa6"/>
    <path d="M0,340 C210,344 360,418 560,500 C720,564 880,578 1096,494 L1096,624 L0,624 Z" fill="#1a5aa6"/>
    <path d="M0,376 C210,382 380,458 570,532 C730,590 900,596 1096,548 L1096,624 L0,624 Z" fill="url(#cyanFill)"/>
  </svg>

  <div class="brand-mark" aria-hidden="true"></div>
  <div class="brand-name">TAVLUNE</div>

  <ul class="contact-list">
    <li class="contact-item contact-address">
      <svg viewBox="0 0 32 32" aria-hidden="true"><circle cx="16" cy="16" r="16" fill="#1a5aa6"/><rect x="8.5" y="11" width="15" height="11" fill="#fff"/><path d="M8.5 11 L16 17 L23.5 11" fill="none" stroke="#1a5aa6" stroke-width="1.4"/></svg>
      <span>240 North Alder Avenue<br>Plano, Texas 75074</span>
    </li>
    <li class="contact-item contact-phone">
      <svg viewBox="0 0 32 32" aria-hidden="true"><circle cx="16" cy="16" r="16" fill="#1a5aa6"/><path d="M10 8.5 L13.5 8 L15 12.5 L13 14 C14 16.5 15.8 18.5 18 19.5 L19.5 17.5 L24 19 L23.5 22.5 C17 24 8.5 15.5 10 8.5 Z" fill="#fff"/></svg>
      <span>800 555 0147</span>
    </li>
    <li class="contact-item contact-fax">
      <svg viewBox="0 0 32 32" aria-hidden="true"><circle cx="16" cy="16" r="16" fill="#1a5aa6"/><rect x="11" y="8" width="10" height="5" fill="#fff"/><rect x="7.5" y="13" width="17" height="8" rx="1.5" fill="#fff"/><rect x="11" y="18" width="10" height="7" fill="#fff" stroke="#1a5aa6" stroke-width="1.2"/></svg>
      <span>928 555 0182</span>
    </li>
    <li class="contact-item contact-web">
      <svg viewBox="0 0 32 32" aria-hidden="true"><circle cx="16" cy="16" r="16" fill="#1a5aa6"/><g fill="none" stroke="#fff" stroke-width="1.4"><circle cx="16" cy="16" r="8.5"/><ellipse cx="16" cy="16" rx="3.8" ry="8.5"/><path d="M7.5 16 H24.5 M9 11.5 H23 M9 20.5 H23"/></g></svg>
      <span>www.tavlune.com</span>
    </li>
  </ul>

  <div class="divider"></div>

  <div class="person">
    <div class="person-name"><strong>MARCUS R.</strong> HOLLOWAY, Ph.D.</div>
    <div class="person-title">PRESIDENT, CTO</div>
  </div>
  <div class="person-email">
    <svg viewBox="0 0 32 32" aria-hidden="true"><circle cx="16" cy="16" r="16" fill="#1a5aa6"/><rect x="8.5" y="11" width="15" height="11" fill="#fff"/><path d="M8.5 11 L16 17 L23.5 11" fill="none" stroke="#1a5aa6" stroke-width="1.4"/></svg>
    <span>marcus.holloway@tavlune.com</span>
  </div>

  <div class="products">
    <div class="products-label">PROVIDERS OF</div>
    <div class="product">CoreVault<sup>TM</sup></div>
    <div class="product">NodeVault<sup>TM</sup></div>
  </div>

  <ul class="services">
    <li class="service">ONLINE PC BACKUP</li>
    <li class="service">CONTINUOUS SERVER BACKUP</li>
    <li class="service">DATA ARCHIVING</li>
  </ul>
</div>
</body>
</html>
```